Business Card Design

We need a new business card design for a CPA office that has been in business for over 10 years. We are a Accounting Concierge firm that offers the following services: Certified Public Accountant, Personal & Business Tax Preparation, Accounting, Bookkeeping, Payroll Services, Tax Litigation Services.
Certified LedgerNest TallyPartner.  We would like to see designs that use the color navy blue in the company logo with classic accent colors.  We would like the card to be on a textured high pound card stock and that is more classic and less modern in design.  The final design should communicate class and professionalism.

Updates
Reason: I gave feedback to many of the designers with some changes.  Please re-read the brief as we would like to remove the photo of the man on the card.  We also want only light grey or white background, not navy or blue - the navy or blue tones should be the font or accent colors.  Please also, consider creating a logo with the initials P&A or PA or P&A CPA.

Industry/Entity Type
Business
Contact Information for Business Card
Pelwick & Associates CPA, Gerald Pelwick III, 5136 Orvale Road West, Suite D, Bradenton, FL  34917, Phone: (555) 318-2276, Fax: (555) 462-7093, Email: Gerald@GPelwickCPA.example, Website: www.GPelwickCPA.example
Requirements
Must have
- LedgerNest Logo

Should not have
- we no longer want the photo on the card.

```html
<!DOCTYPE html>
<html lang="en">
<head>
<meta charset="utf-8">
<title>Pelwick &amp; Associates CPA — Business Card</title>
<link rel="stylesheet" href="https://fonts.googleapis.com/css2?family=Montserrat:wght@300;400;600&display=swap">
<style>
  :root {
    --stage: #e8eaec;
    --card: #ffffff;
    --card-face: #f7f7f5;
    --navy: #0f5a80;
    --navy-deep: #0b4f72;
    --accent-blue: #1b86c4;
    --ink: #184f6e;
    --badge-gold: #e9b520;
  }
  * { box-sizing: border-box; margin: 0; padding: 0; }
  html, body {
    width: 1200px; height: 675px; overflow: hidden;
    background: var(--stage);
    font-family: "Montserrat", Arial, sans-serif;
  }
  .stage { position: relative; width: 1200px; height: 675px; }
  .card {
    position: absolute; top: 188px;
    width: 520px; height: 298px;
    background: var(--card);
    box-shadow: 0 6px 18px rgba(0,0,0,0.12);
    overflow: hidden;
  }
  .card--back { left: 50px; }
  .card--front { left: 630px; background: var(--card-face); }
  .card__base { position: absolute; left: 0; top: 0; }
  .firm-name {
    position: absolute; left: 26px;
    font-weight: 300; font-size: 27px; color: var(--ink);
    letter-spacing: 0.3px; white-space: nowrap;
  }
  .firm-tagline {
    position: absolute; left: 30px;
    font-weight: 400; font-size: 10.5px; color: var(--accent-blue);
    letter-spacing: 5.4px; white-space: nowrap;
  }
  .card--back .firm-name { top: 92px; left: 50px; }
  .card--back .firm-tagline { top: 128px; left: 54px; }
  .card--front .firm-name { top: 30px; }
  .card--front .firm-tagline { top: 66px; }
  .partner-badge {
    position: absolute; left: 420px; top: 64px;
    width: 66px; height: 66px; border-radius: 50%;
    background: var(--badge-gold);
  }
  .person { position: absolute; left: 32px; top: 100px; color: var(--ink); }
  .person__name { font-weight: 600; font-size: 14px; color: var(--navy); }
  .person__role { font-size: 10px; line-height: 13px; margin-top: 4px; }
  .contact {
    position: absolute; left: 32px; top: 168px;
    list-style: none; font-size: 11.5px; line-height: 15px; color: var(--ink);
  }
  .contact li { display: flex; align-items: flex-start; gap: 8px; }
  .contact svg { flex: none; margin-top: 2px; }
  .contact .sep { margin-left: 10px; display: inline-flex; align-items: center; gap: 6px; }
  .website {
    position: absolute; left: 32px; bottom: 7px;
    display: flex; align-items: center; gap: 8px;
    color: #fff; font-size: 12.5px; letter-spacing: 0.3px;
  }
</style>
</head>
<body>
<main class="stage">

  <section class="card card--back" aria-label="Card back">
    <svg class="card__base" width="520" height="298" viewBox="0 0 520 298" aria-hidden="true">
      <polygon points="250,236 520,214 520,222 250,244" fill="var(--accent-blue)"/>
      <polygon points="0,256 300,232 330,244 520,244 520,298 0,298" fill="var(--navy-deep)" transform="translate(0,0)"/>
    </svg>
    <h1 class="firm-name">Pelwick &amp; Associates CPA, LLC</h1>
    <p class="firm-tagline">Full Service Tax and Accounting</p>
  </section>

  <section class="card card--front" aria-label="Card front">
    <svg class="card__base" width="520" height="298" viewBox="0 0 520 298" aria-hidden="true">
      <rect x="240" y="240" width="280" height="7" fill="var(--accent-blue)"/>
      <polygon points="0,240 250,240 275,268 520,268 520,298 0,298" fill="var(--navy-deep)"/>
    </svg>
    <h2 class="firm-name">Pelwick &amp; Associates CPA, LLC</h2>
    <p class="firm-tagline">Full Service Tax and Accounting</p>
    <div class="partner-badge" aria-label="Certified LedgerNest TallyPartner badge"></div>

    <div class="person">
      <p class="person__name">Gerald Pelwick III</p>
      <p class="person__role">Personal &amp; Business<br>Tax Preparation • Accounting</p>
    </div>

    <ul class="contact">
      <li>
        <svg width="10" height="13" viewBox="0 0 10 13"><path d="M5 0a5 5 0 0 1 5 5c0 3.5-5 8-5 8S0 8.5 0 5a5 5 0 0 1 5-5z" fill="var(--accent-blue)"/><circle cx="5" cy="5" r="1.8" fill="#fff"/></svg>
        <span>5136 Orvale Road West, Suite D,<br>Bradenton, FL 34917</span>
      </li>
      <li>
        <svg width="11" height="11" viewBox="0 0 11 11"><path d="M2 0l2 2.5-1 1.3a7 7 0 0 0 3.2 3.2l1.3-1L10 8l-1 2.5C4 10 1 7 .5 2z" fill="var(--accent-blue)"/></svg>
        <span>(555) 318-2276
          <span class="sep"><svg width="12" height="11" viewBox="0 0 12 11"><rect x="0" y="4" width="12" height="7" rx="1" fill="var(--accent-blue)"/><rect x="3" y="0" width="6" height="5" fill="none" stroke="var(--accent-blue)"/></svg>(555) 462-7093</span>
        </span>
      </li>
      <li>
        <svg width="12" height="9" viewBox="0 0 12 9"><rect width="12" height="9" rx="1" fill="var(--accent-blue)"/><path d="M0 1l6 4 6-4" fill="none" stroke="#fff"/></svg>
        <span>Gerald@GPelwickCPA.example</span>
      </li>
    </ul>

    <p class="website">
      <svg width="12" height="12" viewBox="0 0 12 12"><circle cx="6" cy="6" r="5.3" fill="none" stroke="#fff"/><path d="M.7 6h10.6M6 .7c-3 3-3 7.6 0 10.6M6 .7c3 3 3 7.6 0 10.6" fill="none" stroke="#fff" stroke-width=".8"/></svg>
      www.GPelwickCPA.example
    </p>
  </section>

</main>
</body>
</html>
```